Criação de Kit Layout de Posts para Redes Sociais (Facebook, Instagram e etc) para Esportes
" Ofereço serviços de personal trainer para alunos em academias, condomínios, parques, etc.; serviços de personal trainer on-line ao vivo; e serviços de consultoria para prescrição de treinos (sem o acompanhamento durante a execução em si dos treinos) "

```html
<!DOCTYPE html>
<html lang="pt-BR">
<head>
<meta charset="UTF-8">
<title>Treinamento On-line ao Vivo – Rafael Moreira Personal Trainer</title>
<link rel="stylesheet" href="https://fonts.googleapis.com/css2?family=Montserrat:ital,wght@0,600;0,700;0,800;1,800;1,900&display=swap">
<style>
  :root {
    --neon: #39e639;
    --neon-dark: #1f9e2a;
    --ink: #0b0f0c;
    --panel: #ffffff;
    --logo-text: #2f3336;
    --white: #ffffff;
    --shadow: rgba(0,0,0,.75);
  }
  html, body {
    margin: 0;
    padding: 0;
    overflow: hidden;
    background: #111;
  }
  .post {
    position: relative;
    width: 1200px;
    height: 1200px;
    overflow: hidden;
    font-family: "Montserrat", Arial, sans-serif;
    background: var(--ink);
  }
  .hero-photo {
    position: absolute;
    inset: 0;
    background:
      radial-gradient(ellipse 38% 30% at 78% 32%, rgba(190,150,120,.55), transparent 70%),
      radial-gradient(ellipse 55% 16% at 70% 90%, rgba(40,120,200,.75), transparent 75%),
      linear-gradient(180deg, #7a5a4c 0%, #5c463d 40%, #3d3330 65%, #24201f 100%);
  }
  .shapes {
    position: absolute;
    inset: 0;
  }
  .frame {
    position: absolute;
    inset: 0;
    border: 12px solid var(--neon);
    box-sizing: border-box;
    pointer-events: none;
  }
  .frame-stripe {
    position: absolute;
    top: 12px;
    left: 520px;
    right: 12px;
    height: 20px;
    background: repeating-linear-gradient(115deg, var(--ink) 0 22px, var(--neon) 22px 44px);
  }
  .brand-panel {
    position: absolute;
    left: 48px;
    top: 48px;
    width: 528px;
    height: 180px;
    background: var(--panel);
    clip-path: polygon(0 0, 100% 0, 88% 100%, 0 100%);
  }
  .brand-trim {
    position: absolute;
    left: 36px;
    top: 36px;
    width: 560px;
    height: 204px;
    background: var(--neon);
    clip-path: polygon(0 0, 100% 0, 88% 100%, 0 100%);
  }
  .brand-mark {
    position: absolute;
    left: 284px;
    top: 72px;
    width: 54px;
    height: 54px;
    background: var(--neon);
  }
  .brand-name {
    position: absolute;
    left: 60px;
    top: 138px;
    width: 470px;
    text-align: center;
    font-weight: 600;
    font-size: 40px;
    letter-spacing: 1px;
    color: var(--logo-text);
    margin: 0;
  }
  .brand-role {
    position: absolute;
    left: 60px;
    top: 188px;
    width: 470px;
    text-align: center;
    font-weight: 800;
    font-size: 20px;
    letter-spacing: 4px;
    color: var(--neon-dark);
    margin: 0;
  }
  .headline {
    position: absolute;
    left: 54px;
    top: 445px;
    margin: 0;
    font-weight: 900;
    font-style: italic;
    color: var(--white);
    line-height: 1;
    text-shadow: 0 4px 12px var(--shadow);
  }
  .headline-line {
    display: block;
    font-size: 94px;
    letter-spacing: 1px;
  }
  .headline-line + .headline-line { margin-top: 6px; }
  .live-tag {
    display: inline-block;
    vertical-align: 8px;
    margin-left: 18px;
    padding: 8px 22px;
    font-size: 44px;
    font-weight: 800;
    background: #14181a;
    text-shadow: none;
  }
  .question {
    position: absolute;
    left: 66px;
    top: 742px;
    margin: 0;
    font-weight: 900;
    font-style: italic;
    font-size: 52px;
    color: var(--white);
    text-shadow: 0 4px 12px var(--shadow);
  }
  .pitch {
    position: absolute;
    left: 74px;
    top: 815px;
    margin: 0;
    font-weight: 900;
    font-style: italic;
    font-size: 38px;
    line-height: 1.1;
    color: var(--neon);
    text-shadow: 0 3px 10px var(--shadow);
  }
  .contact-cta {
    position: absolute;
    left: 12px;
    top: 980px;
    width: 540px;
    height: 64px;
    background: var(--white);
    clip-path: polygon(0 0, 100% 0, 94% 100%, 0 100%);
    display: flex;
    align-items: center;
    padding-left: 68px;
    box-sizing: border-box;
    font-weight: 900;
    font-style: italic;
    font-size: 34px;
    color: var(--ink);
  }
  .contact-list {
    position: absolute;
    left: 12px;
    top: 1050px;
    width: 560px;
    height: 138px;
    margin: 0;
    padding: 10px 0 0 36px;
    box-sizing: border-box;
    list-style: none;
    background: rgba(10,14,11,.88);
    border-top: 3px solid var(--neon);
    clip-path: polygon(0 0, 100% 0, 92% 100%, 0 100%);
  }
  .contact-item {
    display: flex;
    align-items: center;
    gap: 14px;
    height: 40px;
    font-weight: 700;
    font-size: 25px;
    color: var(--white);
  }
  .contact-icon {
    width: 28px;
    height: 28px;
    flex: none;
  }
</style>
</head>
<body>
<main class="post">
  <div class="hero-photo" role="img" aria-label="Foto de uma mulher fazendo prancha sobre um tapete de yoga azul, em frente a uma parede de tijolos"></div>

  <svg class="shapes" width="1200" height="1200" viewBox="0 0 1200 1200" aria-hidden="true">
    <polygon points="0,0 640,0 180,1200 0,1200" fill="#0b0f0c" opacity=".92"/>
    <polygon points="640,0 760,0 330,1200 180,1200" fill="#0f2a14" opacity=".7"/>
    <polygon points="0,560 520,300 380,1200 0,1200" fill="#102613" opacity=".55"/>
    <line x1="560" y1="420" x2="120" y2="1200" stroke="#39e639" stroke-width="3" opacity=".8"/>
    <line x1="900" y1="380" x2="460" y2="1200" stroke="#39e639" stroke-width="3" opacity=".7"/>
    <line x1="0" y1="760" x2="300" y2="1200" stroke="#39e639" stroke-width="2" opacity=".6"/>
    <line x1="1188" y1="700" x2="980" y2="1188" stroke="#39e639" stroke-width="3" opacity=".7"/>
  </svg>

  <div class="frame"></div>
  <div class="frame-stripe"></div>

  <header>
    <div class="brand-trim"></div>
    <div class="brand-panel"></div>
    <div class="brand-mark"></div>
    <p class="brand-name">RAFAEL MOREIRA</p>
    <p class="brand-role">PERSONAL TRAINER</p>
  </header>

  <h1 class="headline">
    <span class="headline-line">TREINAMENTO</span>
    <span class="headline-line">ON-LINE<span class="live-tag">AO VIVO</span></span>
  </h1>

  <p class="question">ESTÁ SEM TEMPO?</p>
  <p class="pitch">Treina com um profissional<br>&nbsp;sem sair de casa!</p>

  <div class="contact-cta">ENTRE EM CONTATO</div>

  <ul class="contact-list">
    <li class="contact-item">
      <svg class="contact-icon" viewBox="0 0 24 24" aria-hidden="true">
        <circle cx="12" cy="12" r="10.5" fill="none" stroke="#fff" stroke-width="2"/>
        <path d="M8.5 7.5c.5-.5 1.2-.4 1.5.1l1 1.6c.3.5.1 1-.3 1.3l-.6.4c.5 1.2 1.5 2.2 2.7 2.7l.4-.6c.3-.4.9-.6 1.3-.3l1.6 1c.5.3.6 1 .1 1.5l-.8.8c-.7.7-4 .2-6.4-2.2S7 9 7.7 8.3z" fill="#fff"/>
      </svg>
      <span>11 90000-4382</span>
    </li>
    <li class="contact-item">
      <svg class="contact-icon" viewBox="0 0 24 24" aria-hidden="true">
        <circle cx="12" cy="12" r="10.5" fill="#fff"/>
      </svg>
      <span>@personal_rafaelmoreira</span>
    </li>
    <li class="contact-item">
      <svg class="contact-icon" viewBox="0 0 24 24" aria-hidden="true">
        <rect x="2" y="5" width="20" height="14" rx="1.5" fill="#fff"/>
        <path d="M3 6.5l9 6.5 9-6.5" fill="none" stroke="#0b0f0c" stroke-width="1.8"/>
      </svg>
      <span>personal.rafael@mailbox.com</span>
    </li>
  </ul>
</main>
</body>
</html>
```